Software allocation system needs a business card design

We need a business card designed for our software platform - www.plotvane.com.au

At the moment the logo and website is all black and white, we are happy for suggestions on implementing some colour throughout either the logo or business card.

Industry/Entity Type

Software

Font styles to use
Sans Serif

Colors

Designer to choose colors to be used in the design.

```html
<!DOCTYPE html>
<html lang="en">
<head>
<meta charset="utf-8">
<title>Plotvane business card</title>
<link rel="stylesheet" href="https://fonts.googleapis.com/css2?family=Jost:wght@300&family=Lato:wght@400&display=swap">
<style>
  :root {
    --backdrop: #d4d5d7;
    --card-navy: #001f40;
    --wordmark-blue: #0b4e7d;
    --wordmark-faint: #0a3358;
    --band-gold: #d69f13;
    --url-ink: #0b1e3a;
    --icon-blue: #1a9ad9;
    --white: #ffffff;
  }
  * { margin: 0; padding: 0; box-sizing: border-box; }
  html, body {
    width: 1200px;
    height: 1200px;
    overflow: hidden;
    background: var(--backdrop);
  }
  .canvas {
    position: relative;
    width: 1200px;
    height: 1200px;
  }
  .business-card {
    position: absolute;
    left: 109px;
    top: 302px;
    width: 983px;
    height: 594px;
    background: var(--card-navy);
    overflow: hidden;
  }
  .card-art {
    position: absolute;
    inset: 0;
    width: 983px;
    height: 515px;
  }
  .wordmark {
    font-family: "Jost", sans-serif;
    font-weight: 300;
  }
  .wordmark-large { fill: var(--wordmark-blue); font-size: 180px; }
  .wordmark-faint { fill: var(--wordmark-faint); font-size: 40px; }
  .contact-band {
    position: absolute;
    left: 0;
    bottom: 0;
    width: 100%;
    height: 79px;
    background: var(--band-gold);
    display: flex;
    align-items: center;
    justify-content: flex-end;
    padding-right: 86px;
  }
  .website {
    display: flex;
    align-items: center;
    gap: 8px;
    font-family: "Lato", sans-serif;
    font-size: 29px;
    color: var(--url-ink);
  }
  .website-icon { width: 30px; height: 30px; }
</style>
</head>
<body>
<main class="canvas">
  <section class="business-card">
    <svg class="card-art" viewBox="0 0 983 515" aria-hidden="true">
      <text class="wordmark wordmark-faint" x="17" y="146" transform="rotate(-26.5 17 146)" textLength="245" lengthAdjust="spacing">PLOTVANE</text>
      <text class="wordmark wordmark-large" x="101" y="478" transform="rotate(-23.5 101 478)" textLength="830" lengthAdjust="spacing">PLOTVANE</text>
    </svg>
    <footer class="contact-band">
      <p class="website">
        <svg class="website-icon" viewBox="0 0 30 30" aria-hidden="true">
          <circle cx="15" cy="15" r="14" fill="var(--white)"/>
          <circle cx="15" cy="15" r="11" fill="var(--icon-blue)"/>
          <g fill="none" stroke="var(--white)" stroke-width="1.3">
            <circle cx="15" cy="15" r="8"/>
            <ellipse cx="15" cy="15" rx="3.5" ry="8"/>
            <line x1="7" y1="15" x2="23" y2="15"/>
            <line x1="9" y1="10.5" x2="21" y2="10.5"/>
            <line x1="9" y1="19.5" x2="21" y2="19.5"/>
          </g>
        </svg>
        <span>www.plotvane.com.au</span>
      </p>
    </footer>
  </section>
</main>
</body>
</html>
```